Cover design for inventory booklets

As a company we have used a front cover to all our reports which need to include specific information about each property
We therefore need an A4 design design which must allow for inclusion of of the following editable elements through Microsoft Word although I am happy to embed graphical content into Word if not done as part of design process:
Property picture (or pictures if design allows)
Property address
Property size
Agent name (can include logo insert as well if you want)
Job type
Job date
We would like something which appears professional but also acts as a sales tool for the company and repeat business so inclusion of contact details in some form is essential
Style and colours should be derived and be reasonably consistent with those found in our website potentially included the blue tones from the logo and the green of the website as contrast at http://www.quillbrookstays.co.uk/ although please do not let this constrain the designs submitted as we will provide feedback as needed
Target Market(s)
Primary - Letting Agents, Secondary - Landlords and Tenants
Industry/Entity Type
Business

```html
<!DOCTYPE html>
<html lang="en">
<head>
<meta charset="utf-8">
<title>Quillbrook Stays – Inventory Report Cover</title>
<link rel="stylesheet" href="https://fonts.googleapis.com/css2?family=Arimo:wght@400;700&display=swap">
<style>
  :root {
    --navy: #2b2f7f;
    --blue: #2e49a8;
    --ink: #111111;
    --grey: #6b6b6b;
    --paper: #f7f7f7;
    --photo-top: #b9d2ec;
    --photo-bottom: #ddd3c4;
  }
  * { margin: 0; padding: 0; box-sizing: border-box; }
  html, body { width: 927px; height: 1200px; overflow: hidden; }
  body {
    position: relative;
    background: linear-gradient(100deg, #ffffff 0%, var(--paper) 60%, #ebebeb 100%);
    font-family: "Arimo", Arial, sans-serif;
    color: var(--ink);
  }
  .abs { position: absolute; }

  .brand {
    left: 58px; top: 96px;
    display: flex; align-items: center; gap: 14px;
  }
  .brand-dot { width: 18px; height: 18px; background: var(--blue); }
  .brand-name {
    font-size: 46px; font-weight: 400; color: var(--navy);
    letter-spacing: 1px; text-transform: uppercase;
  }

  .call { left: 690px; top: 76px; width: 200px; text-align: center; }
  .call-label { font-size: 46px; line-height: 1.1; }
  .call-number { font-size: 29px; margin-top: 6px; }

  .job-fields { left: 58px; top: 252px; width: 811px; list-style: none; }
  .job-fields li {
    display: flex; align-items: baseline;
    font-size: 29px; font-weight: 700; height: 62px;
  }
  .job-fields li::before { content: "•"; font-size: 22px; margin-right: 14px; }
  .job-fields .fill-line { flex: 1; border-bottom: 2px solid var(--ink); margin-left: 10px; }

  .section-title { left: 58px; top: 549px; font-size: 31px; font-weight: 700; }

  .property-photo {
    left: 534px; top: 452px; width: 335px; height: 218px;
    border: 4px solid var(--blue);
    background: linear-gradient(180deg, var(--photo-top) 0%, var(--photo-bottom) 100%);
  }

  .details { left: 58px; top: 696px; width: 811px; color: var(--grey); }
  .detail { display: flex; font-size: 20px; margin-bottom: 22px; }
  .detail-label { font-size: 28px; font-weight: 700; white-space: nowrap; margin-right: 8px; }
  .detail-label::before { content: "• "; }
  .detail-value { padding-top: 8px; line-height: 26px; }
  .summary { font-size: 20px; line-height: 27px; margin-top: 12px; }

  .footer-band { left: 0; top: 985px; width: 927px; height: 90px; }

  .contact { left: 0; top: 1107px; width: 927px; text-align: center; font-size: 19px; letter-spacing: 1px; }
  .contact-row { display: flex; justify-content: center; gap: 34px; margin-top: 20px; font-size: 18px; }
  .contact-row span { display: flex; align-items: center; gap: 8px; }
</style>
</head>
<body>
  <header>
    <div class="brand abs">
      <span class="brand-dot"></span>
      <span class="brand-name">Quillbrook Stays</span>
    </div>
    <div class="call abs">
      <div class="call-label">Call</div>
      <div class="call-number">08450 555 274</div>
    </div>
  </header>

  <ul class="job-fields abs">
    <li>Agent Name <span class="fill-line"></span></li>
    <li>Job type <span class="fill-line"></span></li>
    <li>Job date <span class="fill-line"></span></li>
  </ul>

  <h2 class="section-title abs">PROPERTY DESCRIPTION</h2>
  <div class="property-photo abs" role="img" aria-label="Property photograph goes here"></div>

  <section class="details abs">
    <div class="detail">
      <span class="detail-label">Property size :</span>
      <span class="detail-value">Lorem Ispum Lorem Ispum</span>
    </div>
    <div class="detail">
      <span class="detail-label">Property Address :</span>
      <span class="detail-value">Lorem Ispum Lorem Ispum Lorem<br>Lorem Ispum Lorem Ispum Lorem<br>Lorem Ispum Lorem Ispum Lorem</span>
    </div>
    <p class="summary">Lorem Ispum Lorem Lorem Ispum Lorem Ispum Lorem Ispum Lorem<br>Lorem Ispum Lorem Ispum Lorem Ispum Lorem Ispum Lorem</p>
  </section>

  <svg class="footer-band abs" viewBox="0 0 927 90" aria-hidden="true">
    <path d="M0 60 C 250 20, 600 20, 927 50 L 927 58 C 600 30, 250 30, 0 70 Z" fill="var(--navy)"/>
  </svg>

  <footer class="contact abs">
    <div>Street Name, City Name, State Name, City Zip Code</div>
    <div class="contact-row">
      <span>
        <svg width="14" height="10" viewBox="0 0 14 10" aria-hidden="true"><rect x="0.5" y="0.5" width="13" height="9" fill="none" stroke="currentColor"/><path d="M0.5 0.5 L7 5.5 L13.5 0.5" fill="none" stroke="currentColor"/></svg>
        mail@quillbrookstays.co.uk
      </span>
      <span>
        <svg width="11" height="11" viewBox="0 0 11 11" aria-hidden="true"><circle cx="5.5" cy="5.5" r="5" fill="currentColor"/></svg>
        www.quillbrookstays.co.uk
      </span>
    </div>
  </footer>
</body>
</html>
```